Harbor Washwell Laundry Service Company

I own a Coin Operated laundry business and need to include a picture of Coin operated machines.
Include:
Company Name: Harbor Washwell
For all your Coin Operated Laundry needs.Include: sales, service, and new installations with commissions as high as 50%
include 1873 N. 9th St, Arcadia, Ca 91006
626-318-7759
Include: Contact: Glen Moravec

Target Market(s)

coin Laundry

Industry/Entity Type

Business

Requirements
Must have
• picture of machines
• Sales, Service, Installations

```html
<!DOCTYPE html>
<html lang="en">
<head>
<meta charset="utf-8">
<title>Harbor Washwell – Postcard</title>
<link rel="stylesheet" href="https://fonts.googleapis.com/css2?family=Source+Sans+3:wght@300;400;600;700&display=swap">
<style>
  :root {
    --page: #efefef;
    --brand-blue: #0a6fba;
    --band-blue: #0b6db8;
    --sky-light: #dceaf7;
    --title-grey: #d9dde2;
    --ink: #1d1d1f;
    --rule: #a9b4bf;
    --white: #ffffff;
  }
  * { box-sizing: border-box; margin: 0; padding: 0; }
  html, body { width: 1037px; height: 1200px; overflow: hidden; }
  body {
    background: var(--page);
    font-family: "Source Sans 3", sans-serif;
    color: var(--ink);
    position: relative;
  }

  /* ---------- Front of card ---------- */
  .card-front {
    position: absolute; left: 69px; top: 60px;
    width: 778px; height: 505px;
    background: linear-gradient(90deg, #e6f0fa 0%, #ffffff 40%, #dfeaf7 100%);
    overflow: hidden;
    box-shadow: 0 2px 8px rgba(0,0,0,.25);
  }
  .front-topstrip {
    position: absolute; left: 0; top: 0; width: 100%; height: 22px;
    background: var(--sky-light);
  }
  .front-band {
    position: absolute; left: 0; top: 22px; width: 100%; height: 94px;
    background: var(--band-blue);
    display: flex; align-items: flex-end; padding: 0 0 16px 27px;
  }
  .brand-title {
    font-weight: 400; font-size: 61px; line-height: 1;
    color: var(--title-grey);
  }
  .band-tagline {
    font-weight: 700; font-size: 18px; color: var(--white);
    margin-left: 18px; margin-bottom: 4px; letter-spacing: .2px;
  }
  .front-waves { position: absolute; left: 0; top: 0; width: 778px; height: 505px; }
  .machine-photo {
    position: absolute; left: 337px; top: 131px; width: 402px; height: 313px;
    background:
      linear-gradient(90deg, rgba(210,216,222,.55) 0%, rgba(255,255,255,0) 4%, rgba(255,255,255,0) 48%, rgba(205,211,218,.7) 50%, rgba(255,255,255,0) 52%, rgba(255,255,255,0) 96%, rgba(210,216,222,.55) 100%),
      linear-gradient(180deg, #eef0f2 0%, #f9fafa 18%, #f3f4f5 60%, #eceeef 100%);
  }
  .front-copy {
    position: absolute; left: 31px; top: 134px; width: 320px;
    font-size: 22.5px; line-height: 27px; font-weight: 400;
  }
  .front-copy .intro { margin-bottom: 39px; }
  .front-copy .include-label { margin-bottom: 2px; }
  .service-list { list-style: none; }
  .service-list li {
    position: relative; padding-left: 25px; margin-bottom: 2px;
    line-height: 27px;
  }
  .service-list .tick-icon {
    position: absolute; left: 0; top: 8px; width: 17px; height: 15px;
  }

  /* ---------- Back of card ---------- */
  .card-back {
    position: absolute; left: 196px; top: 610px;
    width: 777px; height: 501px;
    background: linear-gradient(160deg, #ffffff 35%, #d5e5f5 100%);
    box-shadow: 0 2px 8px rgba(0,0,0,.25);
  }
  .back-divider {
    position: absolute; left: 387px; top: 56px; width: 1px; height: 395px;
    background: var(--rule);
  }
  .back-contact { position: absolute; left: 404px; top: 20px; }
  .back-brand {
    font-size: 29px; font-weight: 400; color: var(--brand-blue);
    line-height: 1.2; margin-bottom: 10px;
  }
  .back-contact p { font-size: 16px; line-height: 18px; }
  .back-contact .contact-person { margin-bottom: 8px; }
  .stamp-box {
    position: absolute; left: 649px; top: 27px; width: 103px; height: 67px;
    border: 1.5px solid var(--rule);
  }
  .address-line {
    position: absolute; left: 422px; width: 329px; height: 1px;
    background: var(--rule);
  }
</style>
</head>
<body>

<section class="card-front">
  <div class="front-topstrip"></div>
  <header class="front-band">
    <h1 class="brand-title">Harbor Washwell</h1>
    <span class="band-tagline">SALES, SERVICE, INSTALLATIONS</span>
  </header>

  <svg class="front-waves" viewBox="0 0 778 505" aria-hidden="true">
    <defs>
      <linearGradient id="waveFill" x1="0" x2="1" y1="0" y2="0">
        <stop offset="0" stop-color="#a6dcf5"/>
        <stop offset="0.5" stop-color="#6aa9df"/>
        <stop offset="1" stop-color="#1f74c8"/>
      </linearGradient>
    </defs>
    <path d="M340 392 C470 395 560 450 778 420" fill="none" stroke="#c7dcf0" stroke-width="1"/>
    <path d="M330 384 C460 388 560 444 778 412" fill="none" stroke="#c7dcf0" stroke-width="1"/>
    <path d="M320 376 C450 380 560 438 778 404" fill="none" stroke="#c7dcf0" stroke-width="1"/>
    <path d="M0 398 C90 376 240 366 380 401 C500 433 620 470 778 440" fill="none" stroke="#bcd9f1" stroke-width="12"/>
    <path d="M0 384 C90 362 240 354 380 390 C500 422 620 458 778 430" fill="none" stroke="#d7e8f7" stroke-width="3"/>
    <path d="M0 416 C90 396 240 386 380 420 C500 450 620 486 778 456 L778 505 L0 505 Z" fill="url(#waveFill)"/>
  </svg>

  <div class="machine-photo" role="img" aria-label="Photo of a coin operated dryer and front-loading washer side by side"></div>

  <div class="front-copy">
    <p class="intro">For all your Coin Operated Laundry needs</p>
    <p class="include-label">INCLUDE:</p>
    <ul class="service-list">
      <li><svg class="tick-icon" viewBox="0 0 17 15" aria-hidden="true"><rect x="1" y="3" width="11" height="11" fill="none" stroke="#1d1d1f" stroke-width="1.5"/><path d="M3.5 8 L6.5 11 L15 1.5" fill="none" stroke="#1d1d1f" stroke-width="1.8"/></svg>Sales</li>
      <li><svg class="tick-icon" viewBox="0 0 17 15" aria-hidden="true"><rect x="1" y="3" width="11" height="11" fill="none" stroke="#1d1d1f" stroke-width="1.5"/><path d="M3.5 8 L6.5 11 L15 1.5" fill="none" stroke="#1d1d1f" stroke-width="1.8"/></svg>Service</li>
      <li><svg class="tick-icon" viewBox="0 0 17 15" aria-hidden="true"><rect x="1" y="3" width="11" height="11" fill="none" stroke="#1d1d1f" stroke-width="1.5"/><path d="M3.5 8 L6.5 11 L15 1.5" fill="none" stroke="#1d1d1f" stroke-width="1.8"/></svg>and new installations with commissions as high as 50%</li>
    </ul>
  </div>
</section>

<section class="card-back">
  <div class="back-contact">
    <h2 class="back-brand">Harbor Washwell</h2>
    <p class="contact-person">Contact: Glen Moravec</p>
    <p>1873 N. 9th St, Arcadia,</p>
    <p>Ca 91006</p>
    <p>p: 626-318-7759</p>
  </div>
  <div class="stamp-box"></div>
  <div class="back-divider"></div>
  <div class="address-line" style="top:212px"></div>
  <div class="address-line" style="top:254px"></div>
  <div class="address-line" style="top:295px"></div>
  <div class="address-line" style="top:337px"></div>
</section>

</body>
</html>
```